Maple Row Yardcare

I want it as prefession and attractive as possible we are a lawnmowing business

Phone number 605-318-2264
Name- Carl Whitby
Email- mapleroweyardsd@fernpost.net

```html
<!DOCTYPE html>
<html lang="en">
<head>
<meta charset="utf-8">
<title>Maple Row Yardcare – Business Card</title>
<link href="https://fonts.googleapis.com/css2?family=Saira+Condensed:wght@600;700;800&display=swap" rel="stylesheet">
<style>
  :root {
    --forest: #0b5d38;
    --leaf: #5bbf3f;
    --paper: #ffffff;
    --backdrop: #e6e8e6;
    --ink-shadow: rgba(0, 0, 0, 0.18);
  }
  * { box-sizing: border-box; margin: 0; padding: 0; }
  html, body {
    width: 1200px;
    height: 900px;
    overflow: hidden;
    background: var(--backdrop);
    font-family: "Saira Condensed", "Arial Narrow", sans-serif;
  }
  .canvas {
    position: relative;
    width: 1200px;
    height: 900px;
  }
  .card {
    position: absolute;
    left: 250px;
    width: 700px;
    height: 400px;
    border-radius: 26px;
    overflow: hidden;
    box-shadow: 0 10px 28px var(--ink-shadow);
  }
  .card--front {
    top: 36px;
    background: var(--forest);
  }
  .card--back {
    top: 464px;
    background: var(--paper);
  }

  /* brand lockup */
  .brand {
    position: absolute;
    display: flex;
    align-items: center;
    gap: 18px;
    font-weight: 800;
    font-size: 66px;
    line-height: 1;
    text-transform: uppercase;
    letter-spacing: 1px;
    white-space: nowrap;
  }
  .brand__square {
    width: 40px;
    height: 40px;
    flex: none;
  }
  .card--front .brand {
    left: 0; right: 0; top: 0; bottom: 0;
    justify-content: center;
    color: var(--paper);
  }
  .card--front .brand__square { background: var(--leaf); }
  .card--back .brand {
    left: 0; right: 0; top: 78px;
    justify-content: center;
    color: var(--forest);
    font-size: 58px;
  }
  .card--back .brand__square { background: var(--leaf); width: 34px; height: 34px; }

  /* contact row */
  .contact {
    position: absolute;
    left: 70px;
    right: 50px;
    top: 226px;
    display: flex;
    align-items: center;
  }
  .contact__name {
    font-weight: 800;
    font-size: 42px;
    text-transform: uppercase;
    letter-spacing: 0.5px;
    white-space: nowrap;
  }
  .contact__first { color: var(--leaf); }
  .contact__last { color: var(--forest); }
  .contact__divider {
    width: 2px;
    height: 62px;
    background: var(--forest);
    margin: 0 24px;
  }
  .contact__list { list-style: none; }
  .contact__item {
    display: flex;
    align-items: center;
    gap: 10px;
    font-weight: 700;
    font-size: 22px;
    color: var(--forest);
    line-height: 1.45;
    white-space: nowrap;
  }
  .contact__icon {
    width: 24px;
    height: 24px;
    flex: none;
  }

  .lawn-edge {
    position: absolute;
    left: 0;
    right: 0;
    bottom: 0;
    height: 70px;
    background: linear-gradient(to bottom, rgba(91,191,63,0) 0%, rgba(91,191,63,0.55) 35%, var(--leaf) 100%);
  }
</style>
</head>
<body>
<main class="canvas">

  <section class="card card--front" aria-label="Card front">
    <div class="brand">
      <span class="brand__square"></span>
      <span class="brand__name">Maple Row Yardcare</span>
    </div>
  </section>

  <section class="card card--back" aria-label="Card back">
    <div class="brand">
      <span class="brand__square"></span>
      <span class="brand__name">Maple Row Yardcare</span>
    </div>

    <div class="contact">
      <p class="contact__name"><span class="contact__first">Carl</span> <span class="contact__last">Whitby</span></p>
      <span class="contact__divider"></span>
      <ul class="contact__list">
        <li class="contact__item">
          <svg class="contact__icon" viewBox="0 0 24 24" aria-hidden="true">
            <circle cx="12" cy="12" r="12" fill="var(--leaf)"/>
            <path d="M8.2 6.5l2 2.3-1.2 1.6c.8 1.7 2 2.9 3.7 3.7l1.6-1.2 2.3 2-1.3 2c-4.6-.4-8.7-4.5-9.1-9.1z" fill="#fff"/>
          </svg>
          605-318-2264
        </li>
        <li class="contact__item">
          <svg class="contact__icon" viewBox="0 0 24 24" aria-hidden="true">
            <circle cx="12" cy="12" r="12" fill="var(--leaf)"/>
            <rect x="6" y="8" width="12" height="8.5" rx="1" fill="#fff"/>
            <path d="M6.5 8.6L12 13l5.5-4.4" fill="none" stroke="var(--leaf)" stroke-width="1.3"/>
          </svg>
          mapleroweyardsd@fernpost.net
        </li>
      </ul>
    </div>

    <div class="lawn-edge" role="img" aria-label="Grass blades growing along the bottom edge of the card"></div>
  </section>

</main>
</body>
</html>
```